School Learner profile graphic representation

I have a set of ideas around communicating our school 'learner profile'. These represent the attitudes, habits and dispositions we are trying to develop through our curriculum and wider enrichment programme. I want the links between the ideas and concepts to be represented in some form of an inforgraphic which can be published and displayed for the whole community to connect with. we run two schools and want the profile to represent for both.

Target Market(s)

Students, Parents, Teachers, Wider community in education

Industry/Entity Type

Education

Font styles to use
Other font styles liked:
• Johnson p22

Colors

Designer to choose colors to be used in the design.

Requirements
Must have
• See my diagram in the ppt.
• The statements Aspiration, Agency, Agility, Altitude with the supporting descriptions. Ideally the values in the center is also represented. The two school logos should also be present somehow (both emblems at least). Let me know if the full logo files are required
Nice to have
• the numbering shown in my diagram is not absolutely necessary is it is not necessarily a linear process and rather cyclical and cross reinforcing

```html
<!DOCTYPE html>
<html lang="en">
<head>
<meta charset="utf-8">
<title>Envisioning Our Learners</title>
<link href="https://fonts.googleapis.com/css2?family=Montserrat:wght@700;800&family=Roboto+Condensed:wght@300;400;700&display=swap" rel="stylesheet">
<style>
  :root {
    --red: #ec1c24;
    --ink: #111111;
    --white: #ffffff;
    --indigo: #4a4a9e;
    --amber: #f9be6c;
    --rose: #ef6c80;
    --lavender: #c2c8e6;
    --navy: #1f2d5a;
    --rule: #e6e9f0;
  }
  * { margin: 0; padding: 0; box-sizing: border-box; }
  html, body { width: 1200px; height: 1200px; overflow: hidden; background: var(--white); }
  .canvas { position: relative; width: 1200px; height: 1200px; background: var(--white); font-family: "Montserrat", sans-serif; }

  .title {
    position: absolute; top: 50px; left: 0; width: 1200px; text-align: center;
    color: var(--red); font-weight: 800; font-size: 67px; letter-spacing: 0.5px; line-height: 1;
  }
  .subtitle {
    position: absolute; top: 133px; left: 0; width: 1200px; text-align: center;
    color: var(--ink); font-weight: 800; font-size: 40px; line-height: 1;
  }

  .pillar { position: absolute; top: 202px; width: 240px; text-align: center; }
  .pillar svg { display: block; margin: 0 auto; }
  .pillar-label { margin-top: 22px; font-weight: 700; font-size: 27px; color: var(--ink); line-height: 1; }
  .pillar--spirit { left: 278px; }
  .pillar--mind { left: 486px; }
  .pillar--heart { left: 702px; }

  .compass {
    position: absolute; left: 896px; top: 288px; width: 224px; height: 224px; border-radius: 50%;
    background: radial-gradient(circle, #7d2b3a 0 6%, #34507a 7% 30%, #ffffff 31% 70%, #1f2d5a 71% 72%, #ffffff 73%);
  }

  .stage { position: absolute; left: 0; top: 0; }

  .illustration {
    position: absolute; left: 392px; top: 412px; width: 424px; height: 336px; border-radius: 50% 50% 40% 40%;
    background: radial-gradient(ellipse at 50% 55%, rgba(74,74,158,0.55), rgba(249,190,108,0.35) 55%, rgba(236,28,36,0) 75%);
  }

  .profile { position: absolute; top: 770px; width: 182px; text-align: center; font-family: "Roboto Condensed", sans-serif; }
  .profile--aspiration { left: 192px; }
  .profile--agency { left: 394px; }
  .profile--agility { left: 596px; }
  .profile--altitude { left: 800px; }
  .profile-lead { color: var(--white); font-weight: 400; font-size: 26px; line-height: 32px; white-space: nowrap; margin: 0 -30px; }
  .profile-name { color: var(--white); font-weight: 700; font-size: 27px; line-height: 32px; white-space: nowrap; margin: 0 -30px; }
  .profile-card {
    margin-top: 14px; height: 194px; border-radius: 8px; padding: 26px 10px 0;
    font-size: 19px; line-height: 24px; font-weight: 400;
  }
  .profile--aspiration .profile-card { background: var(--indigo); color: var(--white); }
  .profile--agency .profile-card { background: var(--amber); color: var(--ink); }
  .profile--agility .profile-card { background: var(--rose); color: var(--white); }
  .profile--altitude .profile-card { background: var(--lavender); color: var(--ink); }

  .footer-rule { position: absolute; left: 180px; top: 1086px; width: 826px; height: 1px; background: var(--rule); }
  .school { position: absolute; top: 1094px; display: flex; align-items: center; gap: 14px; }
  .school--private { left: 218px; }
  .school--community { left: 712px; }
  .school-mark { width: 72px; height: 72px; border-radius: 50%; background: var(--red); flex: none; }
  .school-name { font-family: "Montserrat", sans-serif; font-weight: 700; font-size: 21px; color: var(--ink); line-height: 1.15; }
  .school--community .school-name { color: var(--navy); width: 200px; }
</style>
</head>
<body>
<main class="canvas">
  <h1 class="title">ENVISIONING OUR LEARNERS</h1>
  <h2 class="subtitle">VALUES MORALS PRINCIPLES ETHICS</h2>

  <div class="pillar pillar--spirit">
    <svg width="120" height="120" viewBox="0 0 120 120" aria-hidden="true">
      <circle cx="60" cy="60" r="60" fill="var(--red)"/>
      <g fill="none" stroke="#fff" stroke-width="5" stroke-linejoin="round">
        <rect x="22" y="55" width="14" height="32" rx="2"/>
        <path d="M36 58 L52 40 L54 24 Q62 22 64 32 L62 48 L92 48 Q98 50 96 58 L88 86 Q86 88 82 88 L36 88 Z"/>
        <path d="M62 60 V80 M52 70 H72"/>
      </g>
    </svg>
    <p class="pillar-label">Attitude &amp; Spirit</p>
  </div>

  <div class="pillar pillar--mind">
    <svg width="120" height="120" viewBox="0 0 120 120" aria-hidden="true">
      <circle cx="60" cy="60" r="60" fill="var(--red)"/>
      <path d="M44 100 L44 84 Q26 76 26 54 Q28 26 58 24 Q88 24 92 52 L90 66 L86 80 L72 82 L60 100 Z" fill="#fff"/>
      <circle cx="55" cy="46" r="8" fill="var(--red)"/>
      <circle cx="70" cy="52" r="6" fill="var(--red)"/>
      <circle cx="60" cy="62" r="5" fill="var(--red)"/>
    </svg>
    <p class="pillar-label">Mind</p>
  </div>

  <div class="pillar pillar--heart">
    <svg width="120" height="120" viewBox="0 0 120 120" aria-hidden="true">
      <circle cx="60" cy="60" r="60" fill="var(--red)"/>
      <path d="M60 94 L26 62 Q14 46 26 34 Q42 22 60 40 Q78 22 94 34 Q106 46 94 62 Z" fill="#fff"/>
    </svg>
    <p class="pillar-label">Heart</p>
  </div>

  <div class="compass" role="img" aria-label="Compass rose with north, south, east and west points"></div>

  <svg class="stage" width="1200" height="1200" viewBox="0 0 1200 1200" aria-hidden="true">
    <path d="M146 548 L362 548 A262 262 0 0 1 848 548 L1034 548 Q1050 548 1050 564 L1050 978 Q1050 994 1034 994 L146 994 Q130 994 130 978 L130 564 Q130 548 146 548 Z" fill="var(--red)"/>
  </svg>

  <div class="illustration" role="img" aria-label="Isometric illustration of students around a stack of books, a graduation cap, a flask and a molecule model"></div>

  <section class="profile profile--aspiration">
    <p class="profile-lead">Learners with</p>
    <p class="profile-name">ASPIRATION</p>
    <div class="profile-card">Inspired and Believe in pursuing great things</div>
  </section>
  <section class="profile profile--agency">
    <p class="profile-lead">Learners with</p>
    <p class="profile-name">AGENCY</p>
    <div class="profile-card">Believe in their capacity and responsibility to do great things</div>
  </section>
  <section class="profile profile--agility">
    <p class="profile-lead">Learners with</p>
    <p class="profile-name">AGILITY</p>
    <div class="profile-card">Are determined, equipped and able to to accomplish great things</div>
  </section>
  <section class="profile profile--altitude">
    <p class="profile-lead">Learners with</p>
    <p class="profile-name">ALTITUDE</p>
    <div class="profile-card">Achieve great things and work to elevate others</div>
  </section>

  <div class="footer-rule"></div>
  <div class="school school--private">
    <span class="school-mark"></span>
    <span class="school-name">Cedar Grove Private School</span>
  </div>
  <div class="school school--community">
    <span class="school-mark"></span>
    <span class="school-name">Cedar Grove Community School</span>
  </div>
</main>
</body>
</html>
```